IT services company needs a business card designed

-2 sided business card.-Front is going to be the logo raised (3D floating effect) on a black background. Make the logos spider web shiny silver and keep the spider the same design. -Back needs to have the following information:Darrel Sotho, Managing Partner, Cell: 738-402-1954, Website: Plankhorn.com, Email: Darrel@Plankhorn.com
Target Market(s)
IT Services
Industry/Entity Type
It Company
Contact Information for Business Card
-2 sided business card.
-Front is going to be the logo raised (3D floating effect) on a black background. Make the logos spider web shiny silver and keep the spider the same design.
-Back needs to have the following information:
Darrel Sotho, Managing Partner, Cell: 738-402-1954, Website: Plankhorn.com, Email: Darrel@Plankhorn.com

```html
<!DOCTYPE html>
<html lang="en">
<head>
<meta charset="utf-8">
<title>Plankhorn Business Card</title>
<link href="https://fonts.googleapis.com/css2?family=Open+Sans:wght@400;600;700&display=swap" rel="stylesheet">
<style>
  :root {
    --page-bg: #e9e8e6;
    --card-dark: #2a2d30;
    --pattern-a: #2f3a41;
    --pattern-b: #23282c;
    --card-light: #ffffff;
    --brand-blue: #1ba8e8;
    --ink: #1c1c1c;
    --ink-soft: #3a3a3a;
    --rule: #555555;
  }
  * { box-sizing: border-box; margin: 0; padding: 0; }
  html, body {
    width: 1200px; height: 864px; overflow: hidden;
    background: var(--page-bg);
    font-family: "Open Sans", Arial, sans-serif;
  }
  .stage {
    position: relative; width: 1200px; height: 864px;
    display: flex; align-items: center; justify-content: center; gap: 40px;
  }
  .card {
    position: relative; width: 540px; height: 310px; overflow: hidden;
    box-shadow: 0 6px 18px rgba(0,0,0,0.18);
  }
  /* front */
  .card-front { background: var(--card-dark); }
  .front-pattern {
    position: absolute; inset: 0;
    background: radial-gradient(circle at 40% 40%, var(--pattern-a), var(--pattern-b) 75%);
  }
  .front-mark {
    position: absolute; right: 40px; bottom: 36px;
    display: flex; align-items: center; gap: 8px;
    color: var(--brand-blue); font-weight: 700; font-size: 15px; letter-spacing: 1px;
  }
  .mark-dot { width: 12px; height: 12px; border-radius: 50%; background: var(--brand-blue); }
  /* back */
  .card-back { background: var(--card-light); }
  .person { position: absolute; left: 44px; top: 52px; }
  .person-name {
    color: var(--brand-blue); font-weight: 700; font-size: 22px; text-transform: uppercase; line-height: 1.1;
  }
  .person-title {
    color: var(--ink); font-size: 14px; letter-spacing: 0.5px; text-transform: uppercase; margin-top: 2px;
  }
  .contacts { position: absolute; left: 44px; top: 118px; list-style: none; }
  .contact {
    display: flex; align-items: center; gap: 9px;
    color: var(--ink-soft); font-size: 14px; line-height: 22px;
  }
  .contact svg { width: 14px; height: 14px; flex: none; }
  .rule {
    position: absolute; left: 44px; right: 28px; top: 206px; height: 1px; background: var(--rule);
  }
  .brand {
    position: absolute; right: 36px; top: 132px;
    display: flex; align-items: center; gap: 8px;
    color: var(--ink); font-size: 24px; font-weight: 600; letter-spacing: 1px;
  }
  .brand-dot { width: 14px; height: 14px; border-radius: 50%; background: var(--brand-blue); }
  .band { position: absolute; left: 0; bottom: 0; width: 540px; height: 56px; }
  .band-url {
    position: absolute; right: 36px; bottom: 9px;
    color: #ffffff; font-size: 14px; letter-spacing: 1px;
  }
</style>
</head>
<body>
<main class="stage">
  <section class="card card-front">
    <div class="front-pattern" role="img" aria-label="Repeating pattern of spiders on webs in muted blue over dark grey"></div>
    <div class="front-mark"><span class="mark-dot"></span>PLANKHORN</div>
  </section>

  <section class="card card-back">
    <div class="person">
      <div class="person-name">Darrel Sotho</div>
      <div class="person-title">Managing Partner</div>
    </div>
    <ul class="contacts">
      <li class="contact">
        <svg viewBox="0 0 14 14"><rect x="3" y="0.5" width="8" height="13" rx="1.5" fill="none" stroke="#1ba8e8" stroke-width="1.4"/><rect x="6" y="11" width="2" height="1" fill="#1ba8e8"/></svg>
        738-402-1954
      </li>
      <li class="contact">
        <svg viewBox="0 0 14 14"><rect x="0.5" y="3" width="13" height="9" fill="#1ba8e8"/><path d="M0.5 3 L7 8 L13.5 3" fill="none" stroke="#fff" stroke-width="1.2"/></svg>
        Darrel@Plankhorn.com
      </li>
      <li class="contact">
        <svg viewBox="0 0 14 14"><circle cx="7" cy="7" r="6.5" fill="#1ba8e8"/><path d="M0.5 7 H13.5 M7 0.5 C3.5 4 3.5 10 7 13.5 M7 0.5 C10.5 4 10.5 10 7 13.5" fill="none" stroke="#fff" stroke-width="0.9"/></svg>
        www.Plankhorn.com
      </li>
    </ul>
    <div class="brand"><span class="brand-dot"></span>PLANKHORN</div>
    <div class="rule"></div>
    <svg class="band" viewBox="0 0 540 56">
      <polygon points="0,32 396,32 406,24 540,24 540,56 0,56" fill="#1ba8e8"/>
      <polygon points="0,24 402,24 394,32 0,32" fill="#111111"/>
    </svg>
    <div class="band-url">www.Plankhorn.com</div>
  </section>
</main>
</body>
</html>
```